Identification Supplier website

Front and product page designs required for this Business Catalyst website for an identification supply company.

Also interested in coding same into finished site for additional fee.

Client is a security/event ID supplies company selling identification products like card holders, printers, lanyards, clips and so on.

Current placeholder site is at:
http://www.tagmorrow.com.au/

Other sites the client likes are at:

www.varrowdesigns.com.au

www.badgenook.com.au

www.qrv.com.au

http://start42.brimfield.co.nz/online/welcome.csn

Otherwise colour scheme should follow logo and structure should follow wireframe attached.

Industry/Entity Type

Business

```html
<!DOCTYPE html>
<html lang="en">
<head>
<meta charset="utf-8">
<title>tagmorrow – ID Systems, Supplies, Services and Accessories</title>
<link href="https://fonts.googleapis.com/css2?family=Arimo:wght@400;700&family=Noto+Serif:ital@1&display=swap" rel="stylesheet">
<style>
:root{
  --blue:#1a9ad6;
  --brand:#1f5fa8;
  --dark:#333333;
  --footer:#3a3a3a;
  --black:#0d0d0d;
  --text:#222222;
  --muted:#8a8a8a;
  --line:#dcdcdc;
  --side:#e6eef3;
  --hero:#f1f1f1;
  --page-bg:#f4f4f4;
}
*{margin:0;padding:0;box-sizing:border-box}
html,body{width:973px;height:1200px;overflow:hidden;background:var(--page-bg);font-family:"Arimo",Arial,sans-serif;color:var(--text)}
.page{position:absolute;left:97px;top:0;width:778px;height:1200px;background:#fff}
.abs{position:absolute}

/* header */
.brand{left:10px;top:22px;display:flex;align-items:center;gap:8px}
.brand-dot{width:30px;height:30px;border-radius:50%;background:var(--brand)}
.brand-name{font-size:38px;color:var(--brand);font-weight:400;letter-spacing:.5px}
.tagline{left:229px;top:22px;font-family:"Noto Serif",Georgia,serif;font-style:italic;font-size:18px;color:var(--text)}
.account{right:12px;top:0;width:100px;height:21px;background:var(--blue);color:#fff;font-size:10px;display:flex;align-items:center;justify-content:center;gap:4px}
.phone{right:12px;top:58px;display:flex;align-items:center;gap:8px;font-size:17px;color:var(--text)}
.phone-icon{width:22px;height:22px;background:var(--blue);border-radius:3px;display:flex;align-items:center;justify-content:center}

/* nav */
.nav{left:0;top:92px;width:778px;height:34px;background:var(--dark);display:flex}
.nav a{color:#fff;text-decoration:none;font-size:12.5px;height:34px;display:flex;align-items:center;justify-content:center;border-right:1px solid #555}
.nav a:nth-child(1){width:76px}.nav a:nth-child(2){width:90px}.nav a:nth-child(3){width:112px}
.nav a:nth-child(4){width:109px}.nav a:nth-child(5){width:72px}.nav a:nth-child(6){width:104px}

/* hero */
.hero{left:0;top:126px;width:778px;height:269px;background:var(--hero)}
.hero-title{left:70px;top:44px;font-size:23.5px;color:var(--blue)}
.hero-sub{left:70px;top:70px;font-size:19px;color:var(--text)}
.hero-copy{left:70px;top:116px;width:315px;font-size:11.5px;line-height:14px;color:var(--muted)}
.btn-shop{left:71px;top:193px;width:112px;height:31px;background:var(--blue);color:#fff;font-size:15.5px;display:flex;align-items:center;justify-content:center}
.hero-arrow{top:112px;width:28px;height:45px;background:#8c8c8c;display:flex;align-items:center;justify-content:center}
.hero-visual{left:457px;top:17px;width:232px;height:231px;border-radius:40px 40px 20px 20px;background:linear-gradient(160deg,#2aa9d4,#1a7fb0 45%,#e8ecee 70%,#d9dde0)}

/* catalogue */
.section-title{left:10px;top:418px;font-size:16.5px;color:var(--text)}
.tile{width:174px;height:159px;border:1px solid var(--line);background:#fff}
.tile-img{position:absolute;left:10px;top:8px;width:152px;height:120px;border-radius:6px}
.tile-rule{position:absolute;left:10px;right:10px;top:132px;border-top:1px dotted #b9b9b9}
.tile-name{position:absolute;left:0;right:0;top:139px;text-align:center;font-size:11.3px;color:var(--blue)}

/* sidebar */
.side-box{left:582px;width:187px;background:var(--side)}
.side-title{font-size:14.5px;color:var(--text)}
.news-item{font-size:9.8px;line-height:12px;color:var(--blue);padding:8px 0 8px;border-bottom:1px dotted #b9c7d0}
.news-item b{letter-spacing:.3px}
.signup-copy{font-size:9.8px;line-height:13px;color:#555;margin-top:10px}
.signup-field{display:flex;margin-top:7px;height:24px}
.signup-field span{flex:0 0 139px;background:#fff;border:1px solid #c6ccd0;font-size:10px;padding:6px 0 0 8px}
.signup-field i{flex:0 0 23px;background:var(--brand);display:flex;align-items:center;justify-content:center}
.featured-head{left:582px;top:759px;width:187px;height:32px;background:var(--dark);color:#fff;font-size:17px;padding:6px 0 0 11px}
.featured-body{left:582px;top:791px;width:187px;height:169px;background:#eeeeee}
.featured-img{position:absolute;left:11px;top:10px;width:167px;height:115px;background:#fff;border:1px solid #ccc;display:flex;align-items:center;justify-content:center}
.featured-img div{width:100px;height:90px;border-radius:12px;background:linear-gradient(180deg,#b7b9bb,#6f7275)}
.featured-copy{position:absolute;left:12px;top:132px;width:170px;font-size:9.5px;line-height:11.5px;color:var(--muted)}

/* footer */
.footer{left:0;top:989px;width:778px;height:173px;background:var(--footer)}
.fcol{top:16px}
.fcol h4{font-size:11.5px;font-weight:400;color:#fff;margin-bottom:10px}
.fcol li{list-style:none;font-size:9.8px;color:#cfcfcf;line-height:19.5px;letter-spacing:.3px}
.contact-row{display:flex;gap:8px;font-size:9.8px;line-height:11.5px;color:#cfcfcf;letter-spacing:.3px;margin-bottom:13px}
.contact-row svg{flex:0 0 10px;margin-top:1px}
.footer-brand{left:593px;top:76px;font-size:30px;color:#9a9a9a;display:flex;align-items:center;gap:7px}
.footer-brand span{width:20px;height:20px;border-radius:50%;background:#9a9a9a}
.bottom{left:0;top:1162px;width:778px;height:38px;background:var(--black)}
.copyright{left:14px;top:13px;font-size:9.8px;color:#fff;letter-spacing:.3px}
.social{right:12px;top:8px;display:flex;gap:12px}
.social span{width:20px;height:20px;background:#d6d6d6;border-radius:2px}
</style>
</head>
<body>
<div class="page">

  <header>
    <div class="abs brand"><span class="brand-dot"></span><span class="brand-name">tagmorrow</span></div>
    <div class="abs tagline">ID Systems, Supplies, Services and Accessories</div>
    <div class="abs account"><span>Order Now</span><span>|</span><span>Login</span></div>
    <div class="abs phone">
      <span class="phone-icon"><svg width="12" height="14" viewBox="0 0 12 14"><path d="M3 1 L5 4 L3.8 5.5 Q5 8.5 7.5 10 L9 8.8 L11.5 11 L10 13 Q3 12 1 3 Z" fill="#fff"/></svg></span>
      <span>(03)9000 4172</span>
    </div>
    <nav class="abs nav">
      <a>Home</a><a>About Us</a><a>Our Products</a><a>Our Services</a><a>News</a><a>Contact Us</a>
    </nav>
  </header>

  <section class="abs hero">
    <div class="abs hero-title">Lorem ipsum</div>
    <div class="abs hero-sub">consectetur adipiscing elit</div>
    <p class="abs hero-copy">Lorem ipsum dolor sit amet, consectetur adipiscing elit. Morbi fringilla gravida tempus. Etiam sagittis aliquet erat, ac tristique nunc dignissim nec. Suspendisse sed sodales eros. Donec et tortor lectus, quis bibendum nulla.</p>
    <div class="abs btn-shop">Shop Now</div>
    <div class="abs hero-arrow" style="left:0"><svg width="12" height="24" viewBox="0 0 12 24"><path d="M10 2 L2 12 L10 22" stroke="#fff" stroke-width="2.5" fill="none"/></svg></div>
    <div class="abs hero-arrow" style="left:750px"><svg width="12" height="24" viewBox="0 0 12 24"><path d="M2 2 L10 12 L2 22" stroke="#fff" stroke-width="2.5" fill="none"/></svg></div>
    <div class="abs hero-visual" role="img" aria-label="Blue and white ID card printer with a card being printed"></div>
  </section>

  <main>
    <h2 class="abs section-title" style="font-weight:400">Everything you will ever need in ID Supplies….</h2>

    <div class="abs tile" style="left:10px;top:449px"><div class="tile-img" role="img" aria-label="Card printer with ribbon cartridge" style="background:linear-gradient(135deg,#2a9fd0,#e6eaec)"></div><div class="tile-rule"></div><div class="tile-name">Card Printers And Ribbons</div></div>
    <div class="abs tile" style="left:198px;top:449px"><div class="tile-img" role="img" aria-label="Printed photo ID cards" style="background:linear-gradient(135deg,#2b5fa8,#f2b233)"></div><div class="tile-rule"></div><div class="tile-name">Solutions</div></div>
    <div class="abs tile" style="left:386px;top:449px"><div class="tile-img" role="img" aria-label="Fanned stack of coloured plastic cards" style="background:linear-gradient(135deg,#3a8fd0,#f0c040 55%,#e8e8e8)"></div><div class="tile-rule"></div><div class="tile-name">Bureau Services</div></div>

    <div class="abs tile" style="left:10px;top:622px"><div class="tile-img" role="img" aria-label="Laminating pouches with ID card" style="background:linear-gradient(135deg,#c9d8ea,#e9eef3)"></div><div class="tile-rule"></div><div class="tile-name">Laminates</div></div>
    <div class="abs tile" style="left:198px;top:622px"><div class="tile-img" role="img" aria-label="Assorted printed lanyards" style="background:linear-gradient(135deg,#e0d23a,#d84a3a 50%,#4aa84a)"></div><div class="tile-rule"></div><div class="tile-name">Lanyards</div></div>
    <div class="abs tile" style="left:386px;top:622px"><div class="tile-img" role="img" aria-label="Stack of printed silicone wristbands" style="background:linear-gradient(135deg,#5a3aa0,#f2c12e 45%,#e0502a)"></div><div class="tile-rule"></div><div class="tile-name">Wristbands</div></div>

    <div class="abs tile" style="left:10px;top:795px"><div class="tile-img" role="img" aria-label="Clear plastic card holders" style="background:linear-gradient(135deg,#e3e8ef,#cdd6e2)"></div><div class="tile-rule"></div><div class="tile-name">Card Holders</div></div>
    <div class="abs tile" style="left:198px;top:795px"><div class="tile-img" role="img" aria-label="Badge reels, clips and accessories" style="background:linear-gradient(135deg,#3da640,#8a8f95 50%,#2fb54a)"></div><div class="tile-rule"></div><div class="tile-name" style="font-size:10px">Accessories</div></div>
  </main>

  <aside>
    <div class="abs side-box" style="top:421px;height:200px;padding:11px 11px 0 11px">
      <div class="side-title">Whats New</div>
      <div style="margin-top:7px">
        <div class="news-item"><b>Lorem ipsum dolor sit amet,</b><br>Consectetur adipiscing elit. Vivamus<br>&nbsp;quis turpis dapibus.</div>
        <div class="news-item"><b>Lorem ipsum dolor sit amet,</b><br>Consectetur adipiscing elit. Vivamus<br>&nbsp;quis turpis dapibus.</div>
        <div class="news-item" style="border:0"><b>Lorem ipsum dolor sit amet,</b><br>Consectetur adipiscing elit. Vivamus<br>&nbsp;quis turpis dapibus.</div>
      </div>
    </div>
    <div class="abs side-box" style="top:636px;height:109px;padding:8px 10px 0 10px">
      <div class="side-title">Newsletter Signup</div>
      <p class="signup-copy">Enter your email address below to recieve our monthly newsletter.</p>
      <div class="signup-field"><span>Email address</span><i><svg width="10" height="14" viewBox="0 0 10 14"><path d="M2 1 L8 7 L2 13" stroke="#fff" stroke-width="2.5" fill="none"/></svg></i></div>
    </div>
    <div class="abs featured-head">Featured Products</div>
    <div class="abs featured-body">
      <div class="featured-img" role="img" aria-label="Grey desktop card printer"><div></div></div>
      <p class="featured-copy">Lorem ipsum dolor sit amet, consecte adipiscing elit.</p>
    </div>
  </aside>

  <footer>
    <div class="abs footer">
      <div class="abs fcol" style="left:13px"><h4>Navigation</h4><ul><li>Home</li><li>About Us</li><li>Our Products</li><li>Our Services</li><li>News</li><li>Contact Us</li></ul></div>
      <div class="abs fcol" style="left:139px"><h4>Our Services</h4><ul><li>Suspendisse</li><li>Nullam fermentum</li><li>Integer ornare</li><li>Proin iaculis</li><li>Praesent ac</li></ul></div>
      <div class="abs fcol" style="left:283px"><h4>Our Products</h4><ul><li>Suspendisse</li><li>Nullam fermentum</li><li>Integer ornare</li><li>Proin iaculis</li><li>Praesent ac</li></ul></div>
      <div class="abs fcol" style="left:421px"><h4>Contact us</h4>
        <div class="contact-row" style="margin-top:14px"><svg width="10" height="12" viewBox="0 0 10 12"><path d="M5 0 A4 4 0 0 1 9 4 C9 7 5 12 5 12 C5 12 1 7 1 4 A4 4 0 0 1 5 0Z" fill="#888"/><circle cx="5" cy="4" r="1.5" fill="#3a3a3a"/></svg><span>12/80 Kessel Road, Glen Arbor,<br>Victoria, 3150 Australia</span></div>
        <div class="contact-row" style="margin-top:9px"><svg width="10" height="12" viewBox="0 0 12 14"><path d="M3 1 L5 4 L3.8 5.5 Q5 8.5 7.5 10 L9 8.8 L11.5 11 L10 13 Q3 12 1 3 Z" fill="#888"/></svg><span>(03)9000 4172</span></div>
        <div class="contact-row"><svg width="10" height="10" viewBox="0 0 10 8"><rect x="0" y="0" width="10" height="8" fill="#888"/><path d="M0 0 L5 4.5 L10 0" stroke="#3a3a3a" fill="none"/></svg><span>info@tagmorrow.com.au</span></div>
      </div>
      <div class="abs footer-brand"><span></span>tagmorrow</div>
    </div>
    <div class="abs bottom">
      <div class="abs copyright">Copyright © 2013 tagmorrow. All Right Reserved.</div>
      <div class="abs social"><span aria-label="Social link"></span><span aria-label="Social link"></span><span aria-label="Social link"></span></div>
    </div>
  </footer>

</div>
</body>
</html>
```